Redesign wellness clinic website

The project is redesign a wellness clinic http://www.thornleighvitality.example. The new website is to be responsive,clean,bright and a strong call to action which is to book an appointment. The logo will remain the same but the colour scheme on the website should be reflect purple white and green. I want it to be bright and cheerful and the feeling of clarity. The website shouldn't be overloaded with content but more visuals.

Target Market(s)

Anyone that has corporate wellness benefits within the downtown Toronto core. Majority of audience are professional working in Media, Telecommunications and Investments.

Industry/Entity Type

Health And Wellness

Number of Pages Required

5+ page

Font styles to use
Sans Serif

Colors
ffffff
886aae
acd036

Requirements
Must have
• -Strong call to action which is book an appointment like this page https://www.kestrelmotion.example/
• -Services provided icons on the page like https://www.brightpathvitalityhouse.example/
• - Pictures of a good visualizing a fit and healthy life
• - Strong ratings from Quorva, Zintrel, PostMaz, similar to this website http://www.summitbalancehealth.example/our-team-professionals/
• - Bright and clear
Should not have
• -No black and white images (redo our pictures)
• -Dark themes

```html
<!DOCTYPE html>
<html lang="en">
<head>
<meta charset="utf-8">
<title>Thornleigh Vitality Centre</title>
<link href="https://fonts.googleapis.com/css2?family=Catamaran:wght@600;700&family=Open+Sans:wght@400;600;700&display=swap" rel="stylesheet">
<style>
  :root {
    --purple: #886aae;
    --purple-deep: #7a5ca3;
    --green: #acd036;
    --green-text: #8fb22a;
    --white: #ffffff;
    --ink: #141414;
    --body-ink: #2f2f2f;
    --hero-light: #f4f2f0;
    --hero-warm: #e3c3ac;
  }
  * { box-sizing: border-box; margin: 0; padding: 0; }
  html, body {
    width: 1200px;
    height: 915px;
    overflow: hidden;
    background: var(--white);
  }
  .site {
    position: relative;
    width: 1200px;
    height: 915px;
    background: var(--purple);
    font-family: "Open Sans", sans-serif;
  }
  .brand {
    position: absolute;
    left: 452px;
    top: 0;
    width: 296px;
    height: 96px;
    background: var(--white);
    display: flex;
    align-items: center;
    justify-content: center;
    gap: 12px;
  }
  .brand-dot {
    width: 40px;
    height: 40px;
    border-radius: 50%;
    background: var(--green);
    flex: none;
  }
  .brand-text { display: flex; flex-direction: column; line-height: 1.25; }
  .brand-name {
    font-family: "Open Sans", sans-serif;
    font-weight: 700;
    font-size: 13px;
    color: var(--purple-deep);
  }
  .brand-phone {
    font-family: "Open Sans", sans-serif;
    font-weight: 400;
    font-size: 10px;
    color: var(--green-text);
    padding-left: 38px;
  }
  .main-nav {
    position: absolute;
    left: 60px;
    right: 60px;
    top: 130px;
    height: 70px;
    display: flex;
    align-items: center;
  }
  .nav-list {
    list-style: none;
    display: flex;
    gap: 52px;
    padding-left: 17px;
  }
  .nav-item {
    position: relative;
    font-size: 13px;
    font-weight: 700;
    color: var(--white);
    letter-spacing: 0.2px;
  }
  .nav-item.is-active::before {
    content: "";
    position: absolute;
    left: -17px;
    top: -33px;
    width: 72px;
    height: 4px;
    background: var(--white);
  }
  .nav-search {
    margin-left: auto;
    margin-right: 0;
    width: 26px;
    height: 26px;
  }
  .hero {
    position: absolute;
    left: 60px;
    right: 60px;
    top: 200px;
    bottom: 0;
    overflow: hidden;
  }
  .hero-photo {
    position: absolute;
    inset: 0;
    background:
      radial-gradient(ellipse 45% 35% at 55% 50%, var(--hero-warm) 0%, rgba(227,195,172,0.35) 55%, rgba(244,242,240,0) 100%),
      linear-gradient(180deg, #fbfbfa 0%, var(--hero-light) 55%, #ebe8e6 100%);
  }
  .hero-content {
    position: absolute;
    left: 0;
    right: 0;
    bottom: 90px;
    text-align: center;
  }
  .hero-title {
    font-family: "Catamaran", sans-serif;
    font-weight: 700;
    font-size: 52px;
    line-height: 1;
    color: var(--ink);
    letter-spacing: 0.3px;
  }
  .hero-lead {
    margin-top: 26px;
    font-size: 23px;
    font-weight: 400;
    color: var(--body-ink);
  }
  .cta-book {
    display: inline-block;
    margin-top: 40px;
    width: 370px;
    height: 75px;
    line-height: 69px;
    border: 3px solid var(--purple);
    font-family: "Open Sans", sans-serif;
    font-size: 17px;
    font-weight: 600;
    letter-spacing: 3px;
    color: var(--purple);
    text-decoration: none;
  }
</style>
</head>
<body>
  <div class="site">
    <header class="site-header">
      <div class="brand">
        <span class="brand-dot"></span>
        <div class="brand-text">
          <span class="brand-name">Thornleigh Vitality Centre</span>
          <span class="brand-phone">Call 555-014-0299</span>
        </div>
      </div>
      <nav class="main-nav">
        <ul class="nav-list">
          <li class="nav-item is-active">HOME</li>
          <li class="nav-item">FEES AND SERVICES</li>
          <li class="nav-item">OUR STAFFS</li>
          <li class="nav-item">NEWS &amp; UPDATES</li>
          <li class="nav-item">COPORATE WELLNESS</li>
          <li class="nav-item">FORMS</li>
          <li class="nav-item">CONTACT</li>
        </ul>
        <svg class="nav-search" viewBox="0 0 26 26" aria-label="Search">
          <circle cx="11" cy="11" r="7.5" fill="none" stroke="#ffffff" stroke-width="3"/>
          <line x1="16.5" y1="16.5" x2="23" y2="23" stroke="#ffffff" stroke-width="3.4" stroke-linecap="round"/>
        </svg>
      </nav>
    </header>
    <section class="hero">
      <div class="hero-photo" role="img" aria-label="Photo of a therapist giving a relaxing back massage to a client on a white treatment table"></div>
      <div class="hero-content">
        <h1 class="hero-title">WELCOME TO WELLNESS CENTER</h1>
        <p class="hero-lead">Thornleigh Vitality Centre is a physiotherapist-owned clinic that has built...</p>
        <a class="cta-book" href="#">BOOK AN APPOINMENT</a>
      </div>
    </section>
  </div>
</body>
</html>
```